Graphic Design Project

We are currently undertaking a new business venture. We have developed a business strategy which we wish to present to our prospective business partner as a one page visual.
The business strategy which we developed is in word format. We would like to be able to present our partner with a chart that is more professional visually.
Ideally we would like to be able to edit the document, so that as the strategy changes we can update it - but this is not essential if it hinders the design. Please let us know what format you will be providing the document in.
I have attached a copy of the chart that we created. When we pick the successful design we will send you our company name and logo be included in the design.
Target Market(s)
We are a training company and our new business venture is with another training and development company
Industry/Entity Type
Business
Requirements
Nice to have
- Editable version

```html
<!DOCTYPE html>
<html lang="en">
<head>
<meta charset="utf-8">
<title>Partnership Strategy Flow</title>
<link rel="stylesheet" href="https://fonts.googleapis.com/css2?family=Arimo:ital,wght@0,400;0,700;1,700&display=swap">
<style>
:root{
  --page:#ffffff;
  --band-light:#c9c9ca;
  --band-dark:#4b4b4d;
  --ink:#1f1f1f;
  --white:#ffffff;
  --panel-top:#f4f4f4;
  --panel-bottom:#cfcfd0;
  --blue-a:#2bb1e6;--blue-b:#1a3d7c;
  --orange-a:#ffd21a;--orange-b:#f0741c;
  --purple-a:#9b4aa8;--purple-b:#55175f;
  --green-a:#86c341;--green-b:#2c6428;
  --red-a:#ee2a31;--red-b:#8e1419;
}
*{margin:0;padding:0;box-sizing:border-box}
html,body{width:1200px;height:849px;overflow:hidden;background:var(--page)}
body{font-family:'Arimo',Arial,sans-serif;color:var(--ink);position:relative}
.band{position:absolute;left:0;width:1200px}
.band svg{display:block}
.band--top{top:0}
.band--bottom{bottom:0}

.callout{position:absolute;top:57px;width:143px;height:228px}
.callout svg,.panel svg{position:absolute;inset:0}
.callout__text{position:relative;padding:10px 8px 0;font-size:12.5px;line-height:14.5px;text-align:center}

.stage{position:absolute;top:310px;width:185px;height:162px;border-radius:6px;overflow:hidden;color:var(--white)}
.stage__title{height:33px;line-height:33px;text-align:center;font-weight:700;font-style:italic;font-size:18px;letter-spacing:.5px;background:rgba(0,0,0,.28);border-bottom:1px solid rgba(255,255,255,.35)}
.stage__list{list-style:none;padding:8px 10px 0 10px;font-size:13px;line-height:18px}
.stage__list li{padding-left:14px;position:relative}
.stage__list li::before{content:"";position:absolute;left:2px;top:5px;border-left:7px solid var(--white);border-top:4px solid transparent;border-bottom:4px solid transparent}
.stage--contact{left:30px;background:linear-gradient(160deg,var(--blue-a),var(--blue-b))}
.stage--sales{left:270px;background:linear-gradient(160deg,var(--orange-a),var(--orange-b))}
.stage--solution{left:510px;background:linear-gradient(160deg,var(--purple-a),var(--purple-b))}
.stage--measure{left:747px;background:linear-gradient(160deg,var(--green-a),var(--green-b))}
.stage--roi{left:985px;background:linear-gradient(160deg,var(--red-a),var(--red-b))}

.flow-arrow{position:absolute;top:358px}

.panel{position:absolute;top:490px}
.panel__body{position:relative;padding-top:52px;font-size:12.5px;line-height:15px}
.panel__heading{font-weight:700;font-size:16px;text-align:center;letter-spacing:.5px;margin-bottom:8px}
.panel__item{padding:0 12px;margin-bottom:11px}
.panel--channels-a{left:27px;width:191px;height:305px}
.panel--market{left:262px;width:196px;height:305px}
.panel--market .panel__body{padding-top:48px;font-size:12px;line-height:13px}
.panel--market .panel__heading{margin-bottom:5px}
.panel--market .panel__item{margin-bottom:4px;letter-spacing:-.2px}
.panel--market .divider{margin:4px 0}
.panel--channels-b{left:500px;width:198px;height:162px}
.panel--value{left:757px;width:421px;height:305px}
.panel__intro{padding:78px 16px 0;font-size:12.5px;line-height:16px;height:140px}
.panel__bullets{list-style:none;padding:22px 0 0 24px;font-size:12.5px;line-height:15px}
.panel__bullets li{padding-left:16px;position:relative;margin-bottom:12px}
.panel__bullets li::before{content:"";position:absolute;left:0;top:3px;border-left:7px solid var(--ink);border-top:4px solid transparent;border-bottom:4px solid transparent}
.divider{height:2px;background:var(--white);margin:6px 0}
</style>
</head>
<body>

<div class="band band--top">
  <svg width="1200" height="34" viewBox="0 0 1200 34">
    <polygon points="215,0 1200,0 1200,33 195,33" fill="var(--band-light)"/>
    <polygon points="0,0 200,0 178,33 0,33" fill="var(--band-dark)"/>
  </svg>
</div>

<svg width="0" height="0" style="position:absolute">
  <defs>
    <linearGradient id="greyFill" x1="0" y1="0" x2="0" y2="1">
      <stop offset="0" stop-color="#8e8e90"/><stop offset=".08" stop-color="#d8d8d9"/><stop offset="1" stop-color="#a5a5a7"/>
    </linearGradient>
    <linearGradient id="panelFill" x1="0" y1="0" x2="0" y2="1">
      <stop offset="0" stop-color="#bdbdbe"/><stop offset=".2" stop-color="var(--panel-top)"/><stop offset="1" stop-color="var(--panel-bottom)"/>
    </linearGradient>
    <linearGradient id="gBlue" x1="0" y1="0" x2="1" y2="1"><stop offset="0" stop-color="var(--blue-a)"/><stop offset="1" stop-color="var(--blue-b)"/></linearGradient>
    <linearGradient id="gOrange" x1="0" y1="0" x2="1" y2="1"><stop offset="0" stop-color="var(--orange-a)"/><stop offset="1" stop-color="var(--orange-b)"/></linearGradient>
    <linearGradient id="gPurple" x1="0" y1="0" x2="1" y2="1"><stop offset="0" stop-color="var(--purple-a)"/><stop offset="1" stop-color="var(--purple-b)"/></linearGradient>
    <linearGradient id="gGreen" x1="0" y1="0" x2="1" y2="1"><stop offset="0" stop-color="var(--green-a)"/><stop offset="1" stop-color="var(--green-b)"/></linearGradient>
    <linearGradient id="gRed" x1="0" y1="0" x2="1" y2="1"><stop offset="0" stop-color="var(--red-a)"/><stop offset="1" stop-color="var(--red-b)"/></linearGradient>
  </defs>
</svg>

<div class="callout" style="left:48px">
  <svg width="143" height="228"><polygon points="0,0 143,0 143,186 71.5,228 0,186" fill="url(#greyFill)"/><polygon points="16,188 127,188 71.5,216" fill="url(#gBlue)"/></svg>
  <p class="callout__text">GR- Strategy/tactics<br>OC- Assist to with developing operations and expansion</p>
</div>
<div class="callout" style="left:288px">
  <svg width="143" height="228"><polygon points="0,0 143,0 143,186 71.5,228 0,186" fill="url(#greyFill)"/><polygon points="16,188 127,188 71.5,216" fill="url(#gOrange)"/></svg>
  <p class="callout__text">GR-<br>Develop a new team. Need strong sales people in, and cold callers. Import new capacity</p>
</div>
<div class="callout" style="left:528px">
  <svg width="143" height="228"><polygon points="0,0 143,0 143,186 71.5,228 0,186" fill="url(#greyFill)"/><polygon points="16,188 127,188 71.5,216" fill="url(#gPurple)"/></svg>
  <p class="callout__text">GR-<br>Lean on current and further develop.<br>OC- Technology development: tablet delivery with dashboard<br>OC- Leverage scope</p>
</div>
<div class="callout" style="left:768px">
  <svg width="143" height="228"><polygon points="0,0 143,0 143,186 71.5,228 0,186" fill="url(#greyFill)"/><polygon points="16,188 127,188 71.5,216" fill="url(#gGreen)"/></svg>
  <p class="callout__text">GR-<br>Build on current.<br>OC- develop metrics/ dashboard<br>External: import capacity</p>
</div>
<div class="callout" style="left:1008px">
  <svg width="143" height="228"><polygon points="0,0 143,0 143,186 71.5,228 0,186" fill="url(#greyFill)"/><polygon points="16,188 127,188 71.5,216" fill="url(#gRed)"/></svg>
  <p class="callout__text">Demonstrate and leverage the outcome.</p>
</div>

<section class="stage stage--contact">
  <h2 class="stage__title">CONTACT</h2>
  <ul class="stage__list"><li>Refferrals</li><li>Marketing</li><li>Strong Website</li></ul>
</section>
<section class="stage stage--sales">
  <h2 class="stage__title">SALES</h2>
  <ul class="stage__list"><li>Listening</li><li>Explanation</li><li>Value Prop</li></ul>
</section>
<section class="stage stage--solution">
  <h2 class="stage__title">SOLUTION</h2>
  <ul class="stage__list"><li>Diagnostic</li><li>Funded VET</li><li>EI/ Behaviour</li><li>Consulting: Partner/ Internal</li></ul>
</section>
<section class="stage stage--measure">
  <h2 class="stage__title">MEASUREMENT</h2>
  <ul class="stage__list"><li>Metric Dashboard</li><li>Measure Changes</li><li>Based on Intervention?</li><li>Effect of intervention on Performance</li></ul>
</section>
<section class="stage stage--roi">
  <h2 class="stage__title">ROI</h2>
  <ul class="stage__list"><li>Increased financial performance</li><li>Case Studies</li></ul>
</section>

<svg class="flow-arrow" style="left:219px" width="22" height="58"><polygon points="0,0 22,29 0,58 6,29" fill="url(#gBlue)"/></svg>
<svg class="flow-arrow" style="left:459px" width="22" height="58"><polygon points="0,0 22,29 0,58 6,29" fill="url(#gOrange)"/></svg>
<svg class="flow-arrow" style="left:699px" width="22" height="58"><polygon points="0,0 22,29 0,58 6,29" fill="url(#gPurple)"/></svg>
<svg class="flow-arrow" style="left:937px" width="22" height="58"><polygon points="0,0 22,29 0,58 6,29" fill="url(#gGreen)"/></svg>

<div class="panel panel--channels-a">
  <svg width="191" height="305"><polygon points="0,44 95.5,0 191,44 191,305 0,305" fill="url(#panelFill)"/><polygon points="22,42 95.5,14 169,42" fill="url(#gBlue)"/></svg>
  <div class="panel__body">
    <h3 class="panel__heading">CHANNELS</h3>
    <p class="panel__item">Current- maximise</p>
    <p class="panel__item">Website-improve and increase SEO</p>
    <p class="panel__item">Networks – OC introduce new clients</p>
    <p class="panel__item">Partnership</p>
    <p class="panel__item">Existing Clients</p>
    <p class="panel__item">Private equity – solution sell</p>
    <p class="panel__item">Referrals</p>
  </div>
</div>

<div class="panel panel--market">
  <svg width="196" height="305"><polygon points="0,44 98,0 196,44 196,305 0,305" fill="url(#panelFill)"/><polygon points="22,42 98,14 174,42" fill="url(#gOrange)"/></svg>
  <div class="panel__body">
    <h3 class="panel__heading">MARKET SPLIT</h3>
    <p class="panel__item">Targeting Change: compelling change model</p>
    <p class="panel__item">Projects –Performance Link</p>
    <p class="panel__item">Scale – Genuine mandate for change/growth</p>
    <p class="panel__item">Generating warm leads</p>
    <div class="divider"></div>
    <p class="panel__item">Develop Raving Fans</p>
    <p class="panel__item">Experiential Education Sale</p>
    <div class="divider"></div>
    <p class="panel__item">Work on Model</p>
    <p class="panel__item">Sales team – heavily incentivised</p>
    <p class="panel__item">Solution Sell/Focus</p>
  </div>
</div>

<div class="panel panel--channels-b">
  <svg width="198" height="162"><polygon points="0,44 99,0 198,44 198,162 0,162" fill="url(#panelFill)"/><polygon points="22,42 99,14 176,42" fill="url(#gPurple)"/></svg>
  <div class="panel__body">
    <h3 class="panel__heading">CHANNELS</h3>
    <p class="panel__item">Broaden what we deliver</p>
    <p class="panel__item">i.e. More intensive intervention. Delivery, Behaviour change coaching</p>
  </div>
</div>

<div class="panel panel--value">
  <svg width="421" height="305">
    <polygon points="0,44 98,0 190,44 278,0 421,44 421,305 0,305" fill="url(#panelFill)"/>
    <rect x="0" y="140" width="421" height="2" fill="var(--white)"/>
    <polygon points="22,42 98,14 174,42" fill="url(#gGreen)"/>
    <polygon points="202,42 278,14 354,42" fill="url(#gRed)"/>
  </svg>
  <div class="panel__body" style="padding-top:0">
    <p class="panel__intro">Making the point that training is an investment with a quantifiable outcome. ROI of training very powerful</p>
    <ul class="panel__bullets"><li>Efficiency Gains</li><li>Sales force</li><li>Centralise Functions</li></ul>
  </div>
</div>

<div class="band band--bottom">
  <svg width="1200" height="34" viewBox="0 0 1200 34">
    <rect x="0" y="0" width="1200" height="34" fill="var(--band-light)"/>
    <polygon points="1010,0 1200,0 1200,34 988,34" fill="var(--band-dark)"/>
  </svg>
</div>

</body>
</html>
```